Vehicle Wrapping Company needs a new look

We need to update our website design. We are the largest fleet vehicle wrapping (installation only - we do not print) company in the US. We do not get much business on this site, we use it mainly to update our portfolio/for new clients to see our capabilities. Looking for something modern and clean. We are the innovators in our industry and the best at what we do, our website should represent that. We haven't updated it for a couple years. Our current website: www.varnelwrapworks.com
Industry/Entity Type
Advertising
Coding
Coded - Design and coding required
Number of Pages Required
5+ page
Font styles to use
Other font styles liked:
Look and feel
Each slider illustrates characteristics of the customer's brand and the style your logo design should communicate.

```html
<!DOCTYPE html>
<html lang="en">
<head>
<meta charset="utf-8">
<title>Varnel Wrap Works</title>
<link href="https://fonts.googleapis.com/css2?family=Open+Sans:wght@300;400;600&display=swap" rel="stylesheet">
<style>
:root{
  --orange:#f7941d;
  --orange-dark:#e07f0c;
  --ink:#333;
  --muted:#666;
  --light:#f2f2f2;
  --footer:#3a3a3a;
  --footer-bottom:#2a2a2a;
  --white:#fff;
}
*{box-sizing:border-box;margin:0;padding:0}
html,body{width:1200px;height:2980px;overflow:hidden}
body{font-family:"Open Sans",sans-serif;color:var(--ink);background:var(--white);position:relative}
.topline{height:4px;background:var(--orange)}
.site-header{height:159px;position:relative}
.brand{position:absolute;left:100px;top:50px}
.brand-name{font-size:32px;font-weight:400;color:#222;line-height:1;letter-spacing:.5px}
.header-contact{position:absolute;left:732px;top:46px;display:flex;align-items:center;gap:14px}
.phone-dot{width:44px;height:44px;border-radius:50%;background:var(--orange);display:flex;align-items:center;justify-content:center}
.header-phone{font-size:17px;color:#444;margin-right:40px}
.social{display:flex;gap:8px}
.social span{width:38px;height:38px;border-radius:50%;display:block}
.s1{background:#3b5b98}.s2{background:#3aa6e0}.s3{background:#1a70a8}.s4{background:#2f7fb5}
.main-nav{position:absolute;left:560px;top:108px;display:flex}
.main-nav a{font-size:14px;color:#333;text-decoration:none;padding:0 17px 6px;text-transform:uppercase}
.main-nav a.active{color:var(--orange);border-bottom:2px solid var(--orange);padding-left:0;padding-right:0;margin:0 17px}

.hero{height:513px;position:relative;background:linear-gradient(180deg,#6f9fd0 0%,#a6c4e0 25%,#3f6a3a 38%,#c8262a 48%,#b32024 66%,#5b5b5b 78%,#3b3b3b 100%)}
.hero-arrow{position:absolute;top:238px}
.hero-caption{position:absolute;left:598px;top:363px;color:var(--white)}
.hero-caption h1{font-size:40px;font-weight:300;letter-spacing:1px}
.hero-caption p{font-size:14px;width:520px;line-height:1.55;margin-top:4px}

.services{height:496px;position:relative;text-align:center}
.section-title{font-size:34px;font-weight:300;color:#222;text-transform:uppercase;letter-spacing:.5px}
.section-title em{font-style:normal;color:var(--orange)}
.services .section-title{padding-top:42px}
.lead{font-size:12px;color:var(--muted);line-height:2;width:920px;margin:16px auto 0}
.service-list{position:absolute;top:196px;left:100px;width:1000px;display:flex}
.service{width:250px;text-align:center}
.service-icon{width:110px;height:110px;border-radius:50%;background:var(--orange);margin:0 auto;display:flex;align-items:center;justify-content:center;box-shadow:0 3px 0 var(--orange-dark)}
.service h3{font-size:15px;font-weight:400;margin-top:26px;text-transform:uppercase}
.service p{font-size:11.5px;color:var(--muted);line-height:1.8;width:220px;margin:8px auto 0}
.side-arrow{position:absolute;top:318px}

.about{height:408px;position:relative;text-align:center;color:var(--white);background:linear-gradient(90deg,#2a2a2e 0%,#4a3234 35%,#3e3034 60%,#27282c 100%)}
.about .section-title{color:var(--white);padding-top:98px}
.about p{font-size:13px;width:880px;margin:18px auto 0;line-height:2}
.btn-outline{display:inline-block;margin-top:26px;border:1.5px solid var(--white);border-radius:20px;padding:9px 42px;font-size:13px;letter-spacing:1.5px;color:var(--white)}

.installs{height:914px;text-align:center}
.installs .section-title{padding-top:76px}
.installs .sub{font-size:15px;color:#888;margin-top:10px}
.grid{display:grid;grid-template-columns:repeat(4,300px);margin-top:30px}
.card .photo{height:200px}
.card h4{font-size:12px;font-weight:400;color:#444;margin-top:16px;text-transform:uppercase}
.card p{font-size:12px;color:var(--muted);line-height:1.75;width:240px;margin:6px auto 0;height:64px}
.p1{background:linear-gradient(135deg,#2a1410,#c4581e 55%,#3a1a10)}
.p2{background:linear-gradient(180deg,#8a7a60,#7a2028 55%,#4a4438)}
.p3{background:linear-gradient(180deg,#5a5a5a,#b0b0b4 50%,#6a4030)}
.p4{background:linear-gradient(180deg,#6fa0d8,#f2f2f2 45%,#8a8a8a)}
.p5{background:linear-gradient(180deg,#3a3a3a,#8a8a90 60%,#2a2a2a)}
.p6{background:linear-gradient(180deg,#8aa880,#5fb0c8 45%,#e58a30 70%,#6a6a6a)}
.p7{background:linear-gradient(135deg,#0a1030,#2a4a9a 50%,#0a0a20)}
.p8{background:linear-gradient(180deg,#222,#5a5a5a 55%,#1a1a1a)}
.btn{display:inline-block;margin-top:22px;background:var(--orange);color:var(--white);border-radius:24px;padding:14px 40px;font-size:13px;font-weight:600;letter-spacing:1px}

.partners{height:192px;background:var(--light);position:relative;display:flex;justify-content:center;gap:40px;padding-top:38px}
.badge{width:166px;height:90px;background:var(--white);display:flex;align-items:center;justify-content:center}
.badge span{display:block;width:112px;height:50px;border-radius:4px;background:linear-gradient(180deg,#e4e4e4,#b4b4b8)}

.site-footer{height:240px;background:var(--footer);color:#ddd;position:relative}
.fcol{position:absolute;top:30px}
.fcol h5{font-size:16px;font-weight:400;color:var(--white);text-transform:uppercase;padding-bottom:8px;border-bottom:1px solid #666;width:180px}
.links{list-style:none;margin-top:14px}
.links li{font-size:11px;line-height:23px}
.links li::before{content:"›";margin-right:10px}
.contact-line{display:flex;gap:14px;font-size:11px;line-height:17px;margin-top:14px;align-items:flex-start}
.contact-line.big{font-size:16px}
.news p{font-size:11px;line-height:17px;margin-top:14px;width:220px}
.news .field{width:218px;height:30px;background:var(--white);margin-top:12px;font-size:11px;color:#aaa;padding:7px 10px}
.news .go{display:inline-block;margin-top:12px;background:var(--orange);color:var(--white);font-size:12px;padding:8px 16px}
.post{display:flex;gap:12px;margin-top:14px}
.post .thumb{width:62px;height:60px;background:linear-gradient(135deg,#7a2028,#c8c0b0)}
.post .t{font-size:11px;line-height:19px}
.bottom-bar{height:56px;background:var(--footer-bottom);color:#ccc;font-size:10px;position:relative}
.bottom-bar .copy{position:absolute;left:95px;top:22px}
.bottom-bar .social{position:absolute;left:926px;top:9px}
</style>
</head>
<body>
<div class="topline"></div>
<header class="site-header">
  <div class="brand"><span class="brand-name">VARNEL WRAP WORKS</span></div>
  <div class="header-contact">
    <span class="phone-dot"><svg width="20" height="20" viewBox="0 0 24 24"><path d="M6.6 10.8a15 15 0 0 0 6.6 6.6l2.2-2.2a1 1 0 0 1 1-.25 11.4 11.4 0 0 0 3.6.57 1 1 0 0 1 1 1V20a1 1 0 0 1-1 1A17 17 0 0 1 3 4a1 1 0 0 1 1-1h3.5a1 1 0 0 1 1 1c0 1.25.2 2.45.57 3.57a1 1 0 0 1-.25 1z" fill="#fff"/></svg></span>
    <span class="header-phone">555-318-2046</span>
    <div class="social" aria-label="Social links"><span class="s1"></span><span class="s2"></span><span class="s3"></span><span class="s4"></span></div>
  </div>
  <nav class="main-nav"><a class="active">Home</a><a>About</a><a>Projects</a><a>Portfolio</a><a>Press</a><a>Contact</a></nav>
</header>

<section class="hero" role="img" aria-label="Red tanker truck with a full promotional wrap parked on a lot under blue sky">
  <svg class="hero-arrow" style="left:22px" width="20" height="46"><path d="M18 2 3 23l15 21" stroke="#fff" stroke-width="2" fill="none"/></svg>
  <svg class="hero-arrow" style="right:22px" width="20" height="46"><path d="M2 2l15 21L2 44" stroke="#fff" stroke-width="2" fill="none"/></svg>
  <div class="hero-caption">
    <h1>CERTIFIED PROFESSIONALS</h1>
    <p>Vehicle wraps are being used by companies and car owners to showcase their attention grabbing designs, campaigns or company</p>
  </div>
</section>

<section class="services">
  <h2 class="section-title">What <em>we</em> do</h2>
  <p class="lead">Vehicle wraps are being used by companies and car owners to showcase their attention-grabbing designs, campaigns or company logo(s) with the sole purpose of delivering their messages to the masses.Whether on the road or sailing the high seas, this popular type of promotion connects with viewers at numerous locations such as a busy intersection, different parts of the country or simply gliding past your very own home.</p>
  <svg class="side-arrow" style="left:52px" width="12" height="22"><path d="M10 2 2 11l8 9" stroke="#bbb" stroke-width="2" fill="none"/></svg>
  <svg class="side-arrow" style="right:52px" width="12" height="22"><path d="M2 2l8 9-8 9" stroke="#bbb" stroke-width="2" fill="none"/></svg>
  <div class="service-list">
    <div class="service"><div class="service-icon"><svg width="34" height="38" viewBox="0 0 34 38"><rect x="2" y="2" width="30" height="28" rx="5" fill="#fff"/><rect x="6" y="7" width="22" height="10" fill="#f7941d"/><circle cx="9" cy="24" r="2.5" fill="#f7941d"/><circle cx="25" cy="24" r="2.5" fill="#f7941d"/><rect x="5" y="30" width="5" height="6" fill="#fff"/><rect x="24" y="30" width="5" height="6" fill="#fff"/></svg></div><h3>Buses</h3><p>We make technology easier for you with instant support</p></div>
    <div class="service"><div class="service-icon"><svg width="50" height="32" viewBox="0 0 50 32"><rect x="2" y="4" width="32" height="18" rx="9" fill="#fff"/><path d="M36 8h7l5 7v9H36z" fill="#fff"/><rect x="2" y="22" width="46" height="3" fill="#fff"/><circle cx="10" cy="27" r="4" fill="#fff" stroke="#f7941d" stroke-width="2"/><circle cx="40" cy="27" r="4" fill="#fff" stroke="#f7941d" stroke-width="2"/></svg></div><h3>Tankers</h3><p>The best apps to optimize &amp; secure your digital devices.</p></div>
    <div class="service"><div class="service-icon"><svg width="46" height="30" viewBox="0 0 46 30"><path d="M2 4h28v20H2zM30 10h8l6 7v7H30z" fill="#fff"/><circle cx="10" cy="25" r="4" fill="#fff" stroke="#f7941d" stroke-width="2"/><circle cx="36" cy="25" r="4" fill="#fff" stroke="#f7941d" stroke-width="2"/></svg></div><h3>Vans</h3><p>Many businesses have not learned the value of a professionally designed and maintained</p></div>
    <div class="service"><div class="service-icon"><svg width="38" height="30" viewBox="0 0 38 30"><path d="M8 4h22l5 10v10H3V14z" fill="#fff"/><path d="M10 7h18l3 7H7z" fill="#f7941d"/><circle cx="9" cy="19" r="2.5" fill="#f7941d"/><circle cx="29" cy="19" r="2.5" fill="#f7941d"/><rect x="5" y="24" width="6" height="5" fill="#fff"/><rect x="27" y="24" width="6" height="5" fill="#fff"/></svg></div><h3>Car</h3><p>Many businesses have not learned the value of a professionally designed and maintained</p></div>
  </div>
</section>

<section class="about" role="img" aria-label="Row of wrapped tanker trailers parked beside a warehouse, darkened behind the text">
  <h2 class="section-title">About us</h2>
  <p>Vehicle wraps are being used by companies and car owners to showcase their attention-grabbing designs, campaigns or company logo(s) with the sole purpose of delivering their messages to the masses.Whether on the road or sailing the high seas, this popular type of promotion connects with viewers at numerous locations such as a busy intersection, different parts of the country or simply gliding past your very own home.Many companies, whether big or small, are adopting outdoor advertisement as a means of reaching their target</p>
  <span class="btn-outline">VIEW MORE INFO</span>
</section>

<section class="installs">
  <h2 class="section-title">A few of our <em>latest</em> installs</h2>
  <p class="sub">A successful business needs the competitive edge a professionally designed website offers.</p>
  <div class="grid">
    <article class="card"><div class="photo p1" role="img" aria-label="Two performers on a concert stage with wrapped instruments"></div><h4>2014 Musical Instrument Wraps</h4><p>Having the likes of Jack Rowan or Paper Lanterns play an instrument</p></article>
    <article class="card"><div class="photo p2" role="img" aria-label="Restored cherry red 1950s car"></div><h4>She's My Cherry Pie</h4><p>Old flame lost her spark? Varnel Wrap Works transforms this 1950s Halden</p></article>
    <article class="card"><div class="photo p3" role="img" aria-label="Chrome fuel tanker truck in a service bay"></div><h4>NORCO/ QMART</h4><p>Varnel Wrap Works was selected by Norco Fuels to fully wrap a series</p></article>
    <article class="card"><div class="photo p4" role="img" aria-label="White box trailer with a food distributor wrap"></div><h4>Riverton Symphony Orchestra</h4><p>The cab doors and air shields belonging to the tractors</p></article>
    <article class="card"><div class="photo p5" role="img" aria-label="Silver compact car parked in front of a party banner"></div><h4>Halden Coupe Install</h4><p>An exploration of interactive technology that featured a prime example</p></article>
    <article class="card"><div class="photo p6" role="img" aria-label="Small hatchback with a colourful green and orange wrap"></div><h4>Fernleaf Install</h4><p>We were presented with the opportunity to install a brand new Pelto</p></article>
    <article class="card"><div class="photo p7" role="img" aria-label="Wrapped electric piano on a blue lit stage"></div><h4>Jack Rowan's 2013 Soundwave Awards</h4><p>You might have seen this electric blue piano on stage during Jack Rowan's</p></article>
    <article class="card"><div class="photo p8" role="img" aria-label="Dark sedan on a trade show floor"></div><h4>Showroom Voltra 1</h4><p>A wrap demonstration of the vehicle was featured at this year's Motor Expo</p></article>
  </div>
  <span class="btn">VIEW MORE WORKS</span>
</section>

<section class="partners" aria-label="Partner and certification badges">
  <svg style="position:absolute;left:46px;top:88px" width="10" height="18"><path d="M8 2 2 9l6 7" stroke="#ccc" stroke-width="2" fill="none"/></svg>
  <div class="badge"><span></span></div>
  <div class="badge"><span></span></div>
  <div class="badge"><span></span></div>
  <div class="badge"><span></span></div>
  <div class="badge"><span></span></div>
  <svg style="position:absolute;right:46px;top:88px" width="10" height="18"><path d="M2 2l6 7-6 7" stroke="#ccc" stroke-width="2" fill="none"/></svg>
</section>

<footer class="site-footer">
  <div class="fcol" style="left:95px"><h5>Quick Links</h5>
    <ul class="links"><li>Home</li><li>About</li><li>Projects</li><li>Portfolio</li><li>Press</li><li>Contact</li></ul></div>
  <div class="fcol" style="left:295px"><h5 style="width:250px">Contact Details</h5>
    <div class="contact-line"><svg width="12" height="16" viewBox="0 0 12 16"><path d="M6 0a6 6 0 0 1 6 6c0 4.5-6 10-6 10S0 10.5 0 6a6 6 0 0 1 6-6z" fill="#fff"/><circle cx="6" cy="6" r="2.2" fill="#3a3a3a"/></svg><span>varnelwrapworks.com<br>text of the printing and type<br>setting street-395001</span></div>
    <div class="contact-line big"><svg width="14" height="14" viewBox="0 0 24 24"><path d="M6.6 10.8a15 15 0 0 0 6.6 6.6l2.2-2.2a1 1 0 0 1 1-.25 11.4 11.4 0 0 0 3.6.57 1 1 0 0 1 1 1V20a1 1 0 0 1-1 1A17 17 0 0 1 3 4a1 1 0 0 1 1-1h3.5a1 1 0 0 1 1 1c0 1.25.2 2.45.57 3.57a1 1 0 0 1-.25 1z" fill="#fff"/></svg><span>555-318-2046</span></div>
    <div class="contact-line"><svg width="14" height="11" viewBox="0 0 14 11"><rect width="14" height="11" fill="#fff"/><path d="M0 0l7 6 7-6" stroke="#3a3a3a" fill="none"/></svg><span>info@varnelwrapworks.com</span></div></div>
  <div class="fcol news" style="left:620px"><h5 style="width:220px">Newsletter Signup</h5>
    <p>Having the likes of Jack Rowan or Paper Lanterns play an instrument</p>
    <div class="field">Email address</div>
    <span class="go">Subscribe</span></div>
  <div class="fcol" style="left:900px"><h5 style="width:200px">Our Latest Blog</h5>
    <div class="post"><div class="thumb" role="img" aria-label="Red classic car"></div><div class="t">Old flame lost spark<br>November 01, 2014<br>123 Comments</div></div>
    <div class="post"><div class="thumb" role="img" aria-label="Wrapped vehicle"></div><div class="t">Graphics co-owner<br>November 01, 2014<br>123 Comments</div></div></div>
</footer>
<div class="bottom-bar">
  <span class="copy">Copyright 2016 varnelwrapworks. All Rights Reserved</span>
  <div class="social" aria-label="Social links"><span class="s1"></span><span class="s2"></span><span class="s3"></span><span class="s4"></span></div>
</div>
</body>
</html>
```